Bref créative
Sign for Retail Store
The Velvet Fern Parlour
We need a sign for our retail/service business. Please see attached photos for size.
Retailers
Women over 30, some men.
Our existing logo and colors, which will be uploaded as well.
Logo file .AI

```html
<!DOCTYPE html>
<html lang="en">
<head>
<meta charset="utf-8">
<title>The Velvet Fern Parlour – Storefront Sign</title>
<link rel="stylesheet" href="https://fonts.googleapis.com/css2?family=Comfortaa:wght@500;700&family=Arimo:wght@700&display=swap">
<style>
  :root {
    --sign-black: #000000;
    --fern-green: #8fd400;
    --type-white: #ffffff;
    --backdrop: #ffffff;
  }
  html, body {
    margin: 0;
    padding: 0;
    width: 1200px;
    height: 701px;
    overflow: hidden;
    background: var(--backdrop);
  }
  .sign {
    position: relative;
    width: 1200px;
    height: 701px;
  }
  .sign-frame {
    position: absolute;
    inset: 0;
  }
  .brand-mark {
    position: absolute;
    left: 170px;
    top: 205px;
    width: 150px;
    height: 150px;
    border-radius: 50%;
    background: var(--fern-green);
  }
  .business-name {
    position: absolute;
    left: 440px;
    top: 122px;
    margin: 0;
    font-family: "Comfortaa", sans-serif;
    font-weight: 500;
    font-size: 100px;
    line-height: 0.9;
    letter-spacing: -2px;
    color: var(--type-white);
  }
  .business-name span { display: block; }
  .phone {
    position: absolute;
    left: 0;
    width: 1200px;
    top: 452px;
    text-align: center;
    font-family: "Arimo", sans-serif;
    font-weight: 700;
    font-size: 48px;
    letter-spacing: 4px;
    color: var(--fern-green);
    margin: 0;
  }
  .web-address {
    position: absolute;
    left: 0;
    width: 1200px;
    top: 508px;
    text-align: center;
    font-family: "Arimo", sans-serif;
    font-weight: 700;
    font-size: 19px;
    color: var(--type-white);
    margin: 0;
  }
</style>
</head>
<body>
<main class="sign">
  <svg class="sign-frame" width="1200" height="701" viewBox="0 0 1200 701" aria-hidden="true">
    <!-- rails -->
    <rect class="rail" x="0" y="198" width="1200" height="16" fill="var(--sign-black)"/>
    <rect class="rail" x="0" y="460" width="1200" height="16" fill="var(--sign-black)"/>
    <!-- posts -->
    <rect class="post" x="24" y="112" width="40" height="589" fill="var(--sign-black)"/>
    <rect class="post" x="1134" y="112" width="40" height="589" fill="var(--sign-black)"/>
    <!-- panel -->
    <path class="panel-edge" d="M64 644 V86 H250 Q600 -66 950 86 H1136 V644 Z" fill="var(--sign-black)"/>
    <path class="panel-border" d="M72 636 V94 H252 Q600 -52 948 94 H1128 V636 Z" fill="var(--fern-green)"/>
    <path class="panel-face" d="M92 616 V114 H256 Q600 -28 944 114 H1108 V616 Z" fill="var(--sign-black)"/>
    <path class="panel-inline" d="M108 600 V130 H258 Q600 -6 942 130 H1092 V600 Z" fill="none" stroke="var(--fern-green)" stroke-width="5"/>
    <!-- corner blocks -->
    <g class="corner-blocks" fill="var(--sign-black)" stroke="var(--fern-green)" stroke-width="5">
      <rect x="96" y="118" width="24" height="24"/>
      <rect x="1080" y="118" width="24" height="24"/>
      <rect x="96" y="588" width="24" height="24"/>
      <rect x="1080" y="588" width="24" height="24"/>
    </g>
  </svg>

  <div class="brand-mark" aria-hidden="true"></div>
  <h1 class="business-name">
    <span>The Velvet</span>
    <span>Fern</span>
    <span>Parlour</span>
  </h1>
  <p class="phone">251-555-014</p>
  <p class="web-address">www.thevelvetfernparlour.com</p>
</main>
</body>
</html>
```